Nana Bo's needs your help creating a clean, simple, possibly vintage style label for a natural rem...

We need a label for a new product to be sold in local stores. It will be a bottle of fresh Elderberry Syrup which is a natural remedy for the flu, colds, and allergies. Our syrup is different from others in the market as it is fresh, needs to be refrigerated, and does not include preservatives, added sugar, alcohol, or anything artificial. We would like a label with easy to read text, with a clean or vintage look. We would like a 3 inch by 3 inch circle front label with mostly text, not too busy, and possibly a branch of elderberries may be included. We also need a 3 inch by 3 inch circle label for the back of the bottle with the nutrition facts, ingredients, dosage, and specific text. Both labels should be lighter in (background) color to stand out from the dark purple liquid inside. We're leaning towards black for the main text, but open to other ideas that are neutral and not too flashy.The final design should be clear, clean, making the main text visible if in a grocery store refrigerator. It should appeal to all, but mostly to natural minded mothers.
Natural minded mothers

```html
<!DOCTYPE html>
<html lang="en">
<head>
<meta charset="utf-8">
<title>Nana Bo's Elderberry Syrup Labels</title>
<link rel="stylesheet" href="https://fonts.googleapis.com/css2?family=Cormorant+Garamond:wght@600;700&family=Oswald:wght@300;400;500&family=Arimo:wght@400;700&display=swap">
<style>
:root{
  --page:#e9e8ec;
  --label:#ffffff;
  --purple:#6a2c91;
  --purple-soft:#8a55ad;
  --ink:#222222;
  --leaf:#4f8a3a;
  --berry:#c8202a;
}
*{margin:0;padding:0;box-sizing:border-box}
html,body{width:1200px;height:1072px;overflow:hidden;background:var(--page)}
.canvas{position:relative;width:1200px;height:1072px}
.label{position:absolute;top:266px;width:540px;height:540px}
.label--front{left:40px}
.label--back{left:620px;border-radius:50%;background:var(--label);border:6px solid var(--purple);overflow:hidden;font-family:"Oswald",sans-serif;color:var(--ink)}
.front-svg{width:540px;height:540px;display:block}
.brand-name{font-family:"Cormorant Garamond",serif;font-weight:700;fill:var(--purple)}
.arc-text{font-family:"Oswald",sans-serif;font-weight:400;fill:var(--purple)}
.badge-word{font-family:"Oswald",sans-serif;font-weight:500;fill:var(--purple)}
.badge-net{font-family:"Oswald",sans-serif;font-weight:500;fill:var(--purple)}

.back-art{position:absolute;left:190px;top:20px;width:150px;height:68px;border-radius:40px;background:linear-gradient(90deg,var(--leaf) 0%,var(--berry) 45%,var(--berry) 60%,var(--leaf) 100%)}
.back-claim{position:absolute;left:40px;top:94px;width:448px;text-align:center;font-size:14px;font-weight:300;line-height:20px}
.nutrition{position:absolute;left:34px;top:140px;width:210px;border:1.5px solid var(--ink);padding:3px 4px;font-family:"Arimo",sans-serif;font-size:9px;line-height:10.5px}
.nutrition h3{font-size:24px;line-height:24px;font-weight:700;letter-spacing:-.3px}
.nutrition .rule-thick{border-top:5px solid var(--ink);margin:2px 0}
.nutrition .rule{border-top:1px solid var(--ink)}
.nutrition .row{display:flex;justify-content:space-between;border-top:1px solid var(--ink)}
.nutrition .row.indent{padding-left:12px;border-top:none}
.nutrition .small{font-size:7px}
.nutrition .dv{text-align:right;font-size:7px;font-weight:700}
.disclaimer{position:absolute;left:34px;top:326px;width:210px;border:1.5px solid var(--ink);padding:4px 5px;text-align:center;font-size:11.5px;font-weight:300;line-height:15px}
.info{position:absolute;left:254px;top:140px;width:240px;font-size:12.5px;font-weight:300;line-height:17px}
.info h4{font-size:15px;font-weight:500;line-height:18px}
.info p{margin-bottom:10px}
.info .dosage{font-size:11.5px;line-height:15.5px}
.info .warning{font-size:12px;font-weight:400}
.back-badge{position:absolute;left:110px;top:410px;width:308px;height:80px}
</style>
</head>
<body>
<div class="canvas">

  <section class="label label--front" aria-label="Front label">
    <svg class="front-svg" viewBox="0 0 540 540" xmlns="http://www.w3.org/2000/svg">
      <defs>
        <path id="arc-top" d="M 62,270 A 208 208 0 0 1 478,270"/>
        <path id="arc-bottom" d="M 40,270 A 230 230 0 0 0 500,270"/>
        <linearGradient id="branch-tone" x1="0" x2="1">
          <stop offset="0" stop-color="#4f8a3a"/>
          <stop offset=".45" stop-color="#c8202a"/>
          <stop offset=".6" stop-color="#c8202a"/>
          <stop offset="1" stop-color="#4f8a3a"/>
        </linearGradient>
      </defs>
      <circle cx="270" cy="270" r="264" fill="var(--label)" stroke="var(--purple)" stroke-width="6"/>
      <circle cx="270" cy="270" r="252" fill="none" stroke="var(--purple)" stroke-width="1.2"/>

      <text class="arc-text" font-size="15"><textPath href="#arc-top" startOffset="50%" text-anchor="middle">Immune boosting*, natural remedy for the flu, colds, and allergies*</textPath></text>

      <path d="M 90,160 Q 270,112 450,160" fill="none" stroke="var(--purple)" stroke-width="2"/>
      <rect x="175" y="72" width="190" height="108" rx="50" fill="url(#branch-tone)" role="img" aria-label="Illustration of an elderberry branch with green leaves and red berries"/>

      <text class="brand-name" x="270" y="270" font-size="80" text-anchor="middle">NANA BO'S</text>
      <text class="brand-name" x="270" y="330" font-size="47" text-anchor="middle">ELDERBERRY SYRUP</text>

      <path d="M 95,360 Q 270,345 445,360" fill="none" stroke="var(--purple)" stroke-width="2"/>

      <text class="badge-word" x="165" y="405" font-size="22" text-anchor="middle">Natural</text>
      <line x1="125" y1="412" x2="205" y2="412" stroke="var(--purple)" stroke-width="2"/>
      <circle cx="270" cy="395" r="31" fill="none" stroke="var(--purple)" stroke-width="2.5"/>
      <text class="badge-net" x="270" y="391" font-size="15" text-anchor="middle">NET WT</text>
      <text class="badge-net" x="270" y="409" font-size="15" text-anchor="middle">8 FL OZ</text>
      <text class="badge-word" x="375" y="405" font-size="22" text-anchor="middle">Remedy</text>
      <line x1="335" y1="412" x2="415" y2="412" stroke="var(--purple)" stroke-width="2"/>

      <text class="arc-text" font-size="15"><textPath href="#arc-bottom" startOffset="50%" text-anchor="middle">made with organic elderberries, spices &amp; local Texas raw honey</textPath></text>
    </svg>
  </section>

  <section class="label label--back" aria-label="Back label">
    <div class="back-art" role="img" aria-label="Illustration of an elderberry cluster with leaves"></div>
    <p class="back-claim">This delicious elderberry syrup boosts the immune system.<br>It is a natural remedy for the flu, colds, and allergies.*</p>

    <div class="nutrition">
      <h3>Nutrition Facts</h3>
      <div>Serving Size 1 TBSP</div>
      <div>Servings Per Container 16</div>
      <div class="rule-thick"></div>
      <div class="small"><b>Amount Per Serving</b></div>
      <div class="row"><span><b>Calories</b> 20</span></div>
      <div class="rule-thick" style="border-top-width:3px"></div>
      <div class="dv">% Daily Value*</div>
      <div class="row"><span><b>Total Fat</b> 0g</span><b>0%</b></div>
      <div class="row" style="border-top:none"><span><b>Sodium</b> 4mg</span><b>0%</b></div>
      <div class="row"><span><b>Total Carbohydrate</b> 5g</span><b>2%</b></div>
      <div class="row indent"><span>Sugars 4g</span></div>
      <div class="row"><span><b>Protein</b> 0g</span><b>0%</b></div>
      <div class="rule-thick"></div>
      <div class="small">*Percent Daily Values are based on a 2,000 calorie diet.</div>
    </div>

    <p class="disclaimer">*This statement has not been evaluated by the Food and Drug Administration. This product is not intended to diagnose, treat, cure, or prevent any disease.</p>

    <div class="info">
      <h4>Ingredients</h4>
      <p>Distilled water local Texas raw honey, certified organic elderberries (sambucus nigra), certified organic ginger, certified organic cinnamon, certified organic cloves.</p>
      <p class="dosage">For immune support: Adults 1 tbsp / Children 1 tsp once per day For cold and flu treatment: Take one dose every 2-3 hours</p>
      <p class="warning">DO NOT GIVE TO INFANTS UNDER 1 YEAR OF AGE</p>
      <p class="dosage">Made with love by:<br>Nana Bo's<br>118 Pecan Ln<br>Millbrook, Texas 75990</p>
    </div>

    <svg class="back-badge" viewBox="0 0 308 80" xmlns="http://www.w3.org/2000/svg">
      <text class="badge-word" x="60" y="54" font-size="22" text-anchor="middle">Natural</text>
      <line x1="20" y1="61" x2="100" y2="61" stroke="var(--purple)" stroke-width="2"/>
      <circle cx="154" cy="44" r="31" fill="none" stroke="var(--purple)" stroke-width="2.5"/>
      <text class="badge-net" x="154" y="40" font-size="15" text-anchor="middle">NET WT</text>
      <text class="badge-net" x="154" y="58" font-size="15" text-anchor="middle">8 FL OZ</text>
      <text class="badge-word" x="250" y="54" font-size="22" text-anchor="middle">Remedy</text>
      <line x1="210" y1="61" x2="290" y2="61" stroke="var(--purple)" stroke-width="2"/>
    </svg>
  </section>

</div>
</body>
</html>
```